Invitation - Photos with Santa

We’re doing an event this Christmas for people get photos with Santa.
It’ll be a postcard that we mail to people we know.
Size: 5 x 7, two sided
Details for back of postcard:
Saturday, December 4
10 a.m. - 12 p.m.
18457 Colvin Ln.
Strongsville, OH 44873
The company putting it on is Brightwick. I’ve got a million logo formats so just let me know what you need.
In terms of theme/look/feel for the front of card, I’m a little stuck so I’m open to whatever.
-Skip the line?
-Private Santa party?
-Screw the mall?
Attached is an old one we used last time time we did it.
Let me know if there are any questions!
People I know personally, people with kids, people who private photo with Santa without having to go to the mall

```html
<!DOCTYPE html>
<html lang="en">
<head>
<meta charset="utf-8">
<title>Brightwick – Private Santa Party Postcard</title>
<link href="https://fonts.googleapis.com/css2?family=Montserrat:wght@400;700&family=Kaushan+Script&display=swap" rel="stylesheet">
<style>
  :root {
    --backdrop: #b0b1b0;
    --pine: #06402f;
    --pine-deep: #033526;
    --pine-mid: #0a4a37;
    --leaf: #6fd39a;
    --ember: #e65c1f;
    --crimson: #d71920;
    --snow: #ffffff;
    --ink: #2a2a2a;
    --rule: #333333;
  }
  * { box-sizing: border-box; margin: 0; padding: 0; }
  html, body {
    width: 918px; height: 1200px; overflow: hidden;
    background: var(--backdrop);
    font-family: "Montserrat", sans-serif;
  }
  .postcard {
    position: absolute; left: 173px; width: 601px; height: 430px; overflow: hidden;
  }
  .postcard--front { top: 108px; background: var(--pine); }
  .postcard--back { top: 592px; background: var(--snow); }

  .front-foliage { position: absolute; inset: 0; }

  .brand {
    position: absolute; left: 49px; width: 200px; text-align: center;
    font-weight: 700; color: var(--ember); letter-spacing: -0.3px; line-height: 1;
  }
  .brand-dot { display: block; margin: 0 auto; border-radius: 50%; background: var(--ember); }

  .postcard--front .brand { top: 66px; font-size: 13px; }
  .postcard--front .brand-dot { width: 32px; height: 32px; margin-bottom: 8px; }

  .headline {
    position: absolute; left: 20px; top: 132px; width: 270px;
    font-family: "Kaushan Script", cursive; font-weight: 400; color: var(--snow);
    font-size: 70px; line-height: 58px;
    text-shadow: 0 3px 0 rgba(0,0,0,0.35);
  }
  .headline .line { display: block; white-space: nowrap; }
  .headline .line-1, .headline .line-3 { padding-left: 19px; }
  .headline .mark {
    position: absolute; left: 170px; top: 72px;
    font-size: 160px; line-height: 1;
  }

  .santa-photo {
    position: absolute; left: 296px; top: 98px; width: 305px; height: 332px;
    background: linear-gradient(160deg, var(--ember) 0%, var(--crimson) 55%, #f1f1f1 100%);
    border-radius: 140px 140px 0 0;
  }

  .corner-band { position: absolute; left: 0; top: 0; }

  .event-details { position: absolute; left: 0; top: 0; width: 300px; height: 100%; }
  .postcard--back .brand { top: 56px; font-size: 18px; }
  .postcard--back .brand-dot { width: 54px; height: 54px; margin-bottom: 16px; }
  .detail {
    position: absolute; left: 0; width: 300px; text-align: center;
    color: var(--ink); font-size: 18px; line-height: 25px;
  }
  .detail svg { display: block; margin: 0 auto 8px; }
  .detail--when { top: 176px; }
  .detail--where { top: 274px; }
  .divider {
    position: absolute; left: 300px; top: 30px; width: 1px; height: 370px; background: var(--rule);
  }
</style>
</head>
<body>

<section class="postcard postcard--front" aria-label="Postcard front">
  <svg class="front-foliage" width="601" height="430" viewBox="0 0 601 430">
    <path d="M0 0 L100 0 L8 8 L0 200 Z" fill="var(--ember)"/>
    <path d="M180 0 C260 120 260 300 180 430 L80 430 C160 300 160 120 80 0 Z" fill="var(--pine-mid)"/>
    <path d="M480 0 C560 80 600 200 601 300 L601 0 Z" fill="var(--pine-deep)"/>
    <g role="img" aria-label="Leafy holiday foliage border">
      <rect x="0" y="0" width="601" height="60" fill="var(--pine-deep)" opacity="0.6"/>
      <rect x="0" y="400" width="300" height="30" fill="var(--leaf)" opacity="0.35"/>
      <rect x="450" y="0" width="151" height="80" fill="var(--leaf)" opacity="0.35"/>
    </g>
  </svg>

  <div class="brand"><span class="brand-dot"></span>BRIGHTWICK</div>

  <h1 class="headline">
    <span class="line line-1">Private</span>
    <span class="line line-2">Santa</span>
    <span class="line line-3">party</span>
    <span class="mark">?</span>
  </h1>

  <div class="santa-photo" role="img" aria-label="Photo of Santa taking a selfie with a smiling young boy on his lap"></div>
</section>

<section class="postcard postcard--back" aria-label="Postcard back">
  <svg class="corner-band" width="120" height="160" viewBox="0 0 120 160">
    <path d="M0 0 L110 0 L8 8 L0 150 Z" fill="var(--ember)"/>
  </svg>

  <div class="event-details">
    <div class="brand"><span class="brand-dot"></span>BRIGHTWICK</div>

    <p class="detail detail--when">
      <svg width="14" height="14" viewBox="0 0 14 14" aria-hidden="true">
        <rect x="1" y="2.5" width="11" height="10" rx="1" fill="none" stroke="var(--crimson)" stroke-width="1.2"/>
        <line x1="1" y1="5.5" x2="12" y2="5.5" stroke="var(--crimson)" stroke-width="1.2"/>
        <line x1="4" y1="1" x2="4" y2="4" stroke="var(--crimson)" stroke-width="1.2"/>
        <line x1="9" y1="1" x2="9" y2="4" stroke="var(--crimson)" stroke-width="1.2"/>
      </svg>
      Saturday, December 4<br>10 a.m. - 12 p.m.
    </p>

    <p class="detail detail--where">
      <svg width="14" height="14" viewBox="0 0 14 14" aria-hidden="true">
        <path d="M7 1 C4.5 1 3 3 3 5 C3 7.5 7 11 7 11 C7 11 11 7.5 11 5 C11 3 9.5 1 7 1 Z" fill="none" stroke="var(--crimson)" stroke-width="1.2"/>
        <circle cx="7" cy="5" r="1.4" fill="var(--crimson)"/>
        <path d="M1 13 L3 10 M13 13 L11 10 M1 13 L13 13" stroke="var(--crimson)" stroke-width="1"/>
      </svg>
      18457 Colvin Ln.<br>Strongsville, OH 44873
    </p>
  </div>

  <div class="divider"></div>
</section>

</body>
</html>
```